The Brightwater Compass Business Card

We need an attractive business card with the logo that we bought from ArtVantly last year.
Our mission is to contribute to change the way today's leaders manage business companies bringing value to the workplace and helping them to build a new model of creating wealth.
Our logo is clear about our values : we seek Positive Change through People and are convinced that the pursuit of individual well-being and the chase of economic results can converge with the right management.
Management Consulting
Corinne Fabrelle
+34 612 98 70 31
corinne.fabrelle@thebrightwatercompass-mail.net
www.thebrightwatercompass-mail.net

```html
<!DOCTYPE html>
<html lang="en">
<head>
<meta charset="utf-8">
<title>The Brightwater Compass – Business Card</title>
<link rel="stylesheet" href="https://fonts.googleapis.com/css2?family=Cinzel:wght@400;600&family=Open+Sans:wght@400&display=swap">
<style>
  :root {
    --teal: #128a85;
    --teal-dark: #0e726e;
    --white: #ffffff;
    --ink: #4a4f52;
    --backdrop: #2b2b2d;
    --rule: #1a8f8a;
  }
  * { box-sizing: border-box; margin: 0; padding: 0; }
  html, body {
    width: 1200px; height: 950px; overflow: hidden;
    background: var(--backdrop);
  }
  .sheet {
    width: 1200px; height: 950px;
    display: flex; flex-direction: column; align-items: center; justify-content: center;
    gap: 50px;
  }
  .card {
    position: relative;
    width: 700px; height: 400px;
    overflow: hidden;
  }
  .card--front { background: var(--white); }
  .card--back { background: var(--teal); }

  .brand {
    display: flex; align-items: center; gap: 14px;
    font-family: "Cinzel", serif; font-weight: 600;
    letter-spacing: 1px;
  }
  .brand__dot { border-radius: 50%; flex: none; }

  .card--front .brand {
    position: absolute; top: 58px; right: 48px;
    color: var(--teal); font-size: 26px;
  }
  .card--front .brand__dot { width: 40px; height: 40px; background: var(--teal); }

  .holder {
    position: absolute; left: 48px; top: 170px;
    font-family: "Cinzel", serif; font-weight: 400;
    font-size: 26px; color: var(--teal); letter-spacing: 1px;
  }
  .holder-rule {
    position: absolute; left: 48px; top: 218px;
    width: 420px; height: 1px; background: var(--rule);
  }
  .contacts {
    position: absolute; left: 48px; bottom: 48px;
    list-style: none;
    font-family: "Open Sans", sans-serif; font-size: 14px; color: var(--ink);
  }
  .contacts li { display: flex; align-items: center; gap: 10px; margin-top: 8px; }
  .contacts svg { width: 14px; height: 14px; fill: var(--teal); flex: none; }

  .card--back .brand {
    position: absolute; left: 50%; top: 50%;
    transform: translate(-50%, -50%);
    color: var(--white); font-size: 32px; white-space: nowrap;
  }
  .card--back .brand__dot { width: 52px; height: 52px; background: var(--white); }
</style>
</head>
<body>
<main class="sheet">
  <section class="card card--front" aria-label="Business card front">
    <div class="brand">
      <span class="brand__dot"></span>
      <span class="brand__name">The Brightwater Compass</span>
    </div>
    <h1 class="holder">Corinne Fabrelle</h1>
    <div class="holder-rule"></div>
    <ul class="contacts">
      <li>
        <svg viewBox="0 0 24 24" aria-hidden="true"><path d="M6.6 10.8a15.1 15.1 0 0 0 6.6 6.6l2.2-2.2a1 1 0 0 1 1-.25 11.4 11.4 0 0 0 3.6.57 1 1 0 0 1 1 1V20a1 1 0 0 1-1 1A17 17 0 0 1 3 4a1 1 0 0 1 1-1h3.5a1 1 0 0 1 1 1c0 1.25.2 2.45.57 3.57a1 1 0 0 1-.25 1z"/></svg>
        <span>+34 612 98 70 31</span>
      </li>
      <li>
        <svg viewBox="0 0 24 24" aria-hidden="true"><path d="M2 5h20v14H2z M2 5l10 8 10-8" fill="none" stroke="#128a85" stroke-width="2"/></svg>
        <span>corinne.fabrelle@thebrightwatercompass-mail.net</span>
      </li>
      <li>
        <svg viewBox="0 0 24 24" aria-hidden="true"><circle cx="12" cy="12" r="10"/></svg>
        <span>www.thebrightwatercompass-mail.net</span>
      </li>
    </ul>
  </section>

  <section class="card card--back" aria-label="Business card back">
    <div class="brand">
      <span class="brand__dot"></span>
      <span class="brand__name">The Brightwater Compass</span>
    </div>
  </section>
</main>
</body>
</html>
```